Clean and modern business cards

Looking for an updated business card design for my dental office “corvanta dental” . Looking for a modern clean / sleek design . I’m thinking black background but open to seeing other options . One side needs to have an appointment card . Card needs to have logo, dentist name , phone, email , address . I’ve attached couple of cards I thought were cool as well as my logo
Target Market(s)
Dental patients
Industry/Entity Type
Dentistry
Contact Information for Business Card
Phone email address

```html
<!DOCTYPE html>
<html lang="en">
<head>
<meta charset="utf-8">
<title>Corvanta Dental – Business Card</title>
<link rel="stylesheet" href="https://fonts.googleapis.com/css2?family=Roboto:wght@300;500;700&display=swap">
<style>
  :root {
    --page-bg: #f4f4f4;
    --front-dark: #141414;
    --front-mid: #2a2a2a;
    --front-text: #e6e6e6;
    --back-light: #f3f3f3;
    --back-mid: #dcdcdc;
    --ink: #111111;
    --ink-soft: #222222;
    --rule: #b5b5b5;
    --white: #ffffff;
    --illustration: #c9c9c9;
  }
  * { box-sizing: border-box; margin: 0; padding: 0; }
  html, body {
    width: 1200px; height: 1200px; overflow: hidden;
    background: var(--page-bg);
    font-family: "Roboto", Arial, sans-serif;
  }
  .canvas { position: relative; width: 1200px; height: 1200px; }

  .card {
    position: absolute;
    width: 672px; height: 385px;
    overflow: hidden;
  }

  /* Front */
  .card-front {
    left: 243px; top: 177px;
    background: linear-gradient(135deg, var(--front-mid) 0%, var(--front-dark) 45%, var(--front-mid) 70%, var(--front-dark) 100%);
  }
  .brand-dot {
    position: absolute; left: 300px; top: 40px;
    width: 74px; height: 74px; border-radius: 50%;
    background: var(--front-text);
  }
  .brand-name {
    position: absolute; left: 0; right: 0; top: 160px;
    text-align: center; color: var(--front-text);
    font-weight: 700; font-size: 84px; line-height: 1; letter-spacing: 1px;
  }
  .brand-sub {
    position: absolute; right: 108px; top: 258px;
    color: var(--front-text);
    font-weight: 700; font-size: 36px; line-height: 1; letter-spacing: 16px;
  }
  .front-rule {
    position: absolute; left: 0; right: 0; top: 322px;
    height: 2px; background: var(--white);
  }
  .dentist-tag {
    position: absolute; left: 241px; top: 323px;
    width: 190px; height: 28px;
    background: var(--white); border-radius: 0 0 4px 4px;
    color: var(--ink); font-weight: 500; font-size: 13px;
    display: flex; align-items: center; justify-content: center;
  }

  /* Back */
  .card-back {
    left: 245px; top: 714px; width: 669px; height: 382px;
    background: linear-gradient(120deg, var(--back-light) 0%, #e9e9e9 40%, var(--back-light) 60%, var(--back-mid) 100%);
  }
  .dental-illustration {
    position: absolute; left: 19px; top: 133px;
    width: 102px; height: 152px;
    background: linear-gradient(180deg, var(--illustration), #dedede);
    border-radius: 40px 40px 20px 20px;
    opacity: 0.7;
  }
  .appt-heading {
    position: absolute; left: 0; right: 0; top: 50px;
    text-align: center; padding-left: 60px;
    color: var(--ink); font-weight: 500; font-size: 30px;
  }
  .field {
    position: absolute; left: 145px; width: 440px;
    display: flex; align-items: flex-end;
    color: var(--ink); font-weight: 500; font-size: 19px;
  }
  .field-date { top: 122px; }
  .field-time { top: 168px; left: 146px; }
  .field-line {
    flex: 1; margin-left: 6px; margin-bottom: 5px;
    border-bottom: 1.5px dotted var(--ink-soft);
  }
  .cancel-note {
    position: absolute; left: 151px; top: 222px;
    color: var(--ink); font-weight: 500; font-size: 20px; line-height: 24px;
  }
  .back-rule {
    position: absolute; left: 0; right: 0; top: 299px;
    height: 1px; background: var(--rule);
  }
  .contact {
    position: absolute; left: 0; right: 0; top: 306px;
    text-align: center; padding-right: 1px;
    color: var(--ink-soft); font-weight: 300; font-size: 17px; line-height: 22px;
  }
</style>
</head>
<body>
<main class="canvas">

  <section class="card card-front" aria-label="Business card front">
    <div class="brand-dot"></div>
    <div class="brand-name">CORVANTA</div>
    <div class="brand-sub">DENTAL</div>
    <div class="front-rule"></div>
    <div class="dentist-tag">DR. ELIAS VERHOFF</div>
  </section>

  <section class="card card-back" aria-label="Appointment card back">
    <div class="dental-illustration" role="img" aria-label="Tooth silhouette made of small dental tool icons"></div>
    <h1 class="appt-heading">Your Next Appointment is:</h1>
    <div class="field field-date"><span>DATE</span><span class="field-line"></span></div>
    <div class="field field-time"><span>TIME</span><span class="field-line"></span></div>
    <p class="cancel-note">To cancel or reschedule please notify us at least<br>48 hours prior to your scheduled appointment</p>
    <div class="back-rule"></div>
    <p class="contact">2480 LAKERIDGE AVE, BRANDFIELD, MB | (204) 555-0172<br>CORVANTADENTAL.CA | HELLO@CORVANTADENTAL.CA</p>
  </section>

</main>
</body>
</html>
```